Redesign Our Retail Site (Theme Customization)

We currently have an online store that needs a new design. This design should be based on the Vendara Theme for Cartwisp. Here is our current website:

http://www.lumeswathe.example

We would like to convert it to the Vendara theme:

http://www.vendara.example

The Vendara theme has a simple-to-use control panel that allows you to control all fonts, colors, backgrounds images, and many other things. There is also 1 css stylesheet for doing in-depth customization. It's really easy to use.

For those serious about this project, please contact me and I will send you the Vendara theme so that you can customize it. You will need to install Cartwisp to do this.

We need someone who can give our website some CSS-love. Also, this person needs to be able to design a few main ads, a new background, brush up our logo, and make the color scheme nice and pretty. Make everything tie together.

We will need 3 main ads for the main banner (920 x 320 pixels each). These should say:

"Olympic queen sheets on sale now"
"Twin XL sheets on sale now"
"California King sheets on sale now"

We have already transferred all the product and category data into an Cartwisp/Vendara install here:

http://www.lumeswathe.example/new

If you don't want to install Cartwisp/Vendara just to submit a design, you may just take screen shot of that page, change it up, add a main ad, make it look good, and send it to me if you'd like to submit a design. Eventually, anything submitted this way needs to be transferred to Vendara though.

Thank you very much.

Regards,

Dov Hanstry
LumeSwathe.example
-
Questions? SKYPE ME! - "callerdovhanstry"

Reason: Project was extended 7 days because we decided to guarantee payment and increased budget to $400 1/2 way through due to lack of designs.

Target Market(s)

Adults in USA between the ages of 18 to 40

Industry/Entity Type

Store

Requirements
Must have
• Must be elgant and lovely. Must compliment our name "Lume Swathe" and be playful.

```html
<!DOCTYPE html>
<html lang="en">
<head>
<meta charset="utf-8">
<title>Lume Swathe – Luxury Bed Sheets &amp; Bedding</title>
<link rel="stylesheet" href="https://fonts.googleapis.com/css2?family=Arimo:wght@400;700&family=Nunito:wght@400;700&display=swap">
<style>
:root{
  --page:#ffffff;
  --ink:#3a3a3a;
  --muted:#666666;
  --green:#6aa82c;
  --green-dark:#4f8a1d;
  --teal:#5fb0c9;
  --teal-dark:#2f7f9c;
  --sky:#e3f3fa;
  --sky-edge:#c4e4f1;
  --head-a:#a9d8ec;
  --head-b:#d7eef7;
  --line:#dcdcdc;
  --gray-band:#ececec;
  --star:#f4a51c;
  --star-off:#9a9a9a;
  --orange:#f08a24;
}
*{box-sizing:border-box;margin:0;padding:0}
html,body{width:1200px;height:2330px;overflow:hidden;background:var(--page)}
body{font-family:"Arimo",Arial,sans-serif;color:var(--ink);font-size:13px;position:relative}
a{color:var(--green);text-decoration:none}
.abs{position:absolute}

/* header */
.brand{left:48px;top:58px;display:flex;align-items:center;gap:14px}
.brand-mark{width:68px;height:68px;border-radius:50%;background:var(--teal)}
.brand-name{font-family:"Nunito",sans-serif;font-size:44px;color:var(--green);font-weight:400;line-height:1}
.brand-tag{left:138px;top:108px;font-size:17px;font-weight:700;color:#333}
.shipping{left:596px;top:50px;width:180px;text-align:center}
.shipping b{display:block;color:#7ab6c8;font-size:22px;letter-spacing:.5px}
.shipping span{font-size:13px;font-weight:700}
.ship-badge{left:648px;top:104px;width:70px;height:70px;border-radius:50%;background:var(--orange)}
.currency{left:806px;top:58px;width:150px;height:30px;border:1px solid var(--line);background:#f6f6f6;font-size:12px;color:#888;padding:7px 10px}
.search{left:966px;top:58px;width:185px;height:30px;border:1px solid var(--line);background:#f6f6f6;font-size:13px;padding:7px 10px}
.adv{left:1002px;top:96px;font-size:13px;color:var(--teal-dark)}
.welcome{left:880px;top:137px;font-size:12px;color:#777}
.welcome a{color:var(--teal-dark)}

/* nav */
.nav{left:48px;top:205px;width:1104px;height:52px;border-top:1px solid var(--line);border-bottom:1px solid var(--line);display:flex;align-items:center}
.nav-home{width:72px;display:flex;justify-content:center}
.nav-item{font-size:20px;padding:0 22px;height:44px;line-height:44px;color:#222}
.nav-item.active{background:var(--teal);color:#fff}
.cart{margin-left:auto;display:flex;align-items:center;gap:10px;font-size:17px;font-weight:700;color:var(--teal-dark)}

/* banner */
.banner{left:0;top:270px;width:1200px;height:406px;background:linear-gradient(180deg,var(--sky) 0%,#eef8fc 100%)}
.banner-headline{left:110px;top:350px;font-size:44px;color:var(--teal-dark);font-weight:700}
.banner-copy{left:110px;top:418px;width:260px;font-size:15px;line-height:1.6;color:#555}
.banner-photo{left:640px;top:300px;width:440px;height:330px;border-radius:40% 50% 45% 40%;background:radial-gradient(ellipse at 45% 55%,#a5b3c9 0%,#c7d4e2 45%,rgba(200,225,240,0) 72%)}
.arrow{width:30px;height:44px;background:#fff;border-radius:4px;box-shadow:0 1px 3px rgba(0,0,0,.25);display:flex;align-items:center;justify-content:center}

/* dropdown */
.menu{left:126px;top:257px;width:430px;height:353px;background:#fff;box-shadow:0 3px 10px rgba(0,0,0,.25);padding:14px 18px;display:grid;grid-template-columns:1fr 1fr;column-gap:10px;align-content:start}
.menu h4{font-size:13px;font-weight:700;margin:10px 0 6px;grid-column:span 2}
.menu h4.half{grid-column:auto}
.menu ul{list-style:none}
.menu li{font-size:11px;line-height:18px;padding-left:12px;position:relative}
.menu li::before{content:"";position:absolute;left:2px;top:6px;border-left:5px solid var(--green);border-top:3px solid transparent;border-bottom:3px solid transparent}

/* content */
.panel-head{height:44px;background:linear-gradient(180deg,var(--head-a),var(--head-b));font-size:20px;font-weight:700;color:#1d3f55;padding:11px 14px;border:1px solid var(--sky-edge)}
.sidebar{left:48px;top:748px;width:298px;border:1px solid var(--sky-edge)}
.cat-list{list-style:none;background:linear-gradient(180deg,#f2f9fc,#fff);padding:8px 0 10px}
.cat-list li{font-size:14px;font-weight:700;height:32.5px;line-height:32.5px;padding-left:44px;position:relative;border-bottom:1px dotted #d3e6ee}
.cat-list li::before{content:"";position:absolute;left:20px;top:11px;width:11px;height:11px;border-radius:50%;background:#8c9aa0}
.cat-list li.sub{padding-left:66px;font-weight:400}
.cat-list li.sub::before{left:44px;width:8px;height:8px;top:12px;background:none;border-left:6px solid var(--green);border-top:4px solid transparent;border-bottom:4px solid transparent;border-radius:0}
.welcome-box{left:366px;top:748px;width:786px;height:745px;border:1px solid var(--sky-edge)}
.welcome-body{padding:12px 14px;font-size:12.6px;line-height:1.5;color:#444}
.welcome-body p{margin-bottom:6px}
.photo-right{float:right;width:200px;height:140px;margin:4px 0 6px 14px}
.sizes{display:grid;grid-template-columns:1fr 1fr;width:520px;margin:4px 0 6px 96px;font-weight:700;color:var(--green);line-height:1.55}

/* products */
.section-title{left:48px;top:1496px;font-size:22px;font-weight:700;color:#222}
.rule{left:48px;top:1528px;width:1104px;border-top:1px solid var(--line)}
.card{top:1550px;width:250px;text-align:center}
.card-photo{height:170px;border:1px solid var(--line);padding:6px;background:#fff}
.card-photo div{width:100%;height:100%}
.card h5{font-size:17px;font-weight:700;margin:14px 0 8px;color:#222}
.stars{display:flex;justify-content:center;gap:2px}

/* footer band */
.band{left:0;top:1830px;width:1200px;height:406px;background:var(--gray-band)}
.col-title{font-size:19px;color:#555;padding-bottom:10px;border-bottom:1px dotted #bbb;display:flex;align-items:center;gap:10px}
.tips{left:48px;top:1862px;width:548px}
.tip{display:flex;gap:14px;margin-top:18px;font-size:13px;line-height:1.55;color:#555}
.tip-num{flex:none;width:36px;height:36px;border-radius:50%;background:#fff;border:1px solid #ccc;font-size:20px;color:#888;text-align:center;line-height:34px}
.chirp{left:630px;top:1862px;width:268px}
.tweet{display:flex;gap:12px;margin-top:16px;font-size:12.5px;line-height:1.5;color:#555}
.tweet .q{font-size:36px;color:#bbb;line-height:.8;font-family:Georgia,serif}
.tweet small{color:#888;font-size:12px}
.fans{left:928px;top:1862px;width:224px}
.fans p{font-size:12px;color:#666;margin:14px 0 10px}
.fan-grid{display:grid;grid-template-columns:repeat(3,1fr);row-gap:10px;text-align:center}
.fan-grid span{display:block;width:44px;height:44px;margin:0 auto 5px;background:linear-gradient(180deg,#cdd5da,#8c979e);border:2px solid #fff}
.fan-grid div{font-size:11px;color:#555}
.foot-links{left:0;top:2264px;width:1200px;text-align:center;font-size:13px;color:#555}
.foot-links a{color:#555;margin:0 8px}
.copy{left:0;top:2290px;width:1200px;text-align:center;font-size:12px;color:#777}
</style>
</head>
<body>

<!-- header -->
<div class="abs brand"><span class="brand-mark"></span><span class="brand-name">Lume Swathe</span></div>
<div class="abs brand-tag">Luxury Bed Sheets &amp; Bedding</div>
<div class="abs shipping"><b>FREE SHIPPING</b><span>all orders over $150</span></div>
<div class="abs ship-badge"></div>
<div class="abs currency">Euro</div>
<div class="abs search">Search</div>
<a class="abs adv">Advance Search</a>
<div class="abs welcome">Welcome visitor you can <a>login</a> or <a>create an account</a>.</div>

<nav class="abs nav">
  <span class="nav-home"><svg width="30" height="26" viewBox="0 0 30 26"><path d="M15 2 2 13h4v11h7v-7h4v7h7V13h4z" fill="#222"/></svg></span>
  <span class="nav-item active">King bedding</span>
  <span class="nav-item">Queen bedding</span>
  <span class="nav-item">Learning center</span>
  <span class="nav-item">Contact Us</span>
  <span class="cart"><svg width="28" height="24" viewBox="0 0 28 24"><path d="M1 2h5l3 13h14l3-9H8" fill="none" stroke="#2f7f9c" stroke-width="2.5"/><circle cx="11" cy="20" r="2.3" fill="#2f7f9c"/><circle cx="21" cy="20" r="2.3" fill="#2f7f9c"/></svg>Your Cart <span style="font-weight:400;color:#333">(0 item)</span></span>
</nav>

<!-- banner -->
<section class="abs banner" aria-label="Main banner">
  <svg class="abs" style="left:0;top:0" width="1200" height="12"><path d="M0 0h1200v4q-6 8-12 0t-12 0t-12 0" fill="#fff"/><pattern id="scallop" width="12" height="12" patternUnits="userSpaceOnUse"><path d="M0 0h12v3q-6 8-12 0z" fill="#fff"/></pattern><rect width="1200" height="12" fill="url(#scallop)"/></svg>
</section>
<div class="abs banner-headline">Olympic queen sheets on sale</div>
<div class="abs banner-copy">Lorem ipsum soft sheets now at a lower price</div>
<div class="abs banner-photo" role="img" aria-label="Folded grey striped bed sheets with a light blue swirl decoration"></div>
<div class="abs arrow" style="left:12px;top:468px"><svg width="12" height="18"><path d="M10 2 3 9l7 7" fill="none" stroke="#222" stroke-width="3"/></svg></div>
<div class="abs arrow" style="left:1158px;top:468px"><svg width="12" height="18"><path d="M2 2l7 7-7 7" fill="none" stroke="#222" stroke-width="3"/></svg></div>

<div class="abs menu">
  <h4>California King Bedding</h4>
  <ul><li>California King Sheets</li><li>California King Bed In A Bags</li><li>California King Bedskirts</li></ul>
  <ul><li>California King Comforters</li><li>California King Duvet Covers</li><li>California King Mattress Pads</li></ul>
  <h4>King Bedding</h4>
  <ul><li>King Sheets</li><li>King Bed In A Bags</li><li>King Bedskirts</li><li>King Comforters</li></ul>
  <ul><li>King Duvet Covers</li><li>King Featherbeds</li><li>King Mattress Pads</li></ul>
  <h4 class="half">Split King Bedding</h4><h4 class="half">Split California King Bedding</h4>
  <ul><li>Split King Sheets</li></ul>
  <ul><li>Split California King Sheets</li></ul>
  <h4>Super King Bedding</h4>
  <ul><li>Super King Sheets</li></ul>
</div>

<!-- sidebar -->
<aside class="abs sidebar">
  <div class="panel-head" style="border:0">Most Popular Bedding</div>
  <ul class="cat-list">
    <li>Waterbed Sheets</li>
    <li class="sub">Hard-Side Waterbed Sheets</li>
    <li class="sub">Soft-Side Waterbed Sheets</li>
    <li>Flat or Fitted Sheets Only</li>
    <li>Bed In A Bag Sets</li>
    <li>Extra Deep Pocket Sheets</li>
    <li>Pillows</li>
    <li>Pillow Cases and Shams</li>
    <li>Bamboo Sheets</li>
    <li>Flannel Sheets</li>
    <li>Microfiber Sheets</li>
    <li>Extra Long Bedskirts</li>
    <li>Throws</li>
    <li>Miscellaneous</li>
  </ul>
</aside>

<!-- welcome -->
<section class="abs welcome-box">
  <div class="panel-head" style="border:0">Welcome to Lume Swathe</div>
  <div class="welcome-body">
    <p>Where do worries sink away, washed over by serenity? Where does comfort sedate the stress of life? Where can joy and laughter be shared no matter what you're wearing? Where do you let yourself go completely and utterly? You surrender to your bed each day, in the wash of night, when time resets itself for another go-round. And not just your bed, but everything on and around it.</p>
    <div class="photo-right" role="img" aria-label="Bedroom with a navy and white made bed" style="background:linear-gradient(160deg,#c9b89a,#3a4a7a 55%,#e8e8ee)"></div>
    <p>At Lume Swathe, we provide solutions for all your bedding needs. You owe yourself the tranquility and nurturing rest that our premium bedding products facilitate. You deserve the soothing comfort of our quality bedding and sheets. You can sleep wrapped in bedding fit for royalty. You can burrow under one of our plush comforters. You can enhance your existing mattress with our choice of mattress pads. Or, perfect your sanctuary's decor with one of our <a>bedskirts</a>. You'll find fitting accessories for nearly every <a>bed size</a> at Lume Swathe.</p>
    <p>Take advantage of our extensive knowledge and let us guide you to more pleasurable bedding experiences. Use our menus above to explore the possibilities for your bed. You can also shop by size using the links below:</p>
    <div class="sizes">
      <span>King <span style="color:#444">and</span> Split King</span><span>Full, Full XL, <span style="color:#444">and</span> Full XXL</span>
      <span>Queen <span style="color:#444">and</span> Split Queen</span><span>Hospital Sizes</span>
      <span>Olympic Queen <span style="color:#444">and</span> California Queen</span><span>Super Single</span>
      <span>California King <span style="color:#444">... and</span> Super King</span><span>Twin XL <span style="color:#444">and</span> Twin XXL<span style="color:#444">(for college dorms)</span></span>
    </div>
    <p>If you can't find what you're looking for, please email us at <a><b>support@lumeswathe.example</b></a> and we can coordinate custom bedding for your Sample bedding set. needs. So you can make the best purchase possible, and to help you design the perfect bedding experience, read some of our <a><b>Bedding Articles</b></a> or the <a><b>Linen Learning Center</b></a> located at the bottom-left of every page on the site. There's more to it than you might think. Check it out now.</p>
    <div class="photo-right" role="img" aria-label="Bright bedroom with a cream made bed" style="background:linear-gradient(160deg,#efe6d6,#cdbb9c 55%,#f6f1e8)"></div>
    <p>At Lume Swathe, we have a passion for the bedding experience that benefits you, the customer. If you need any help finding the best products for your bed, shoot us an email or use the form on the <a><b>Contact Us</b></a> page. You can find a link to it at the top-right of every page on our site. We're updating our inventory constantly so you should check back often. Some treats we're really looking forward to in the future are an increased collection of quality dust ruffles, feather beds, and down products. We also look forward to adding more great Pima (Suprena) cotton products. Contact us for wholesale options if you have bulk purchase needs.</p>
  </div>
</section>

<!-- top products -->
<h3 class="abs section-title">Top Products</h3>
<div class="abs rule"></div>
<div class="abs arrow" style="left:12px;top:1610px"><svg width="12" height="18"><path d="M10 2 3 9l7 7" fill="none" stroke="#222" stroke-width="3"/></svg></div>
<div class="abs arrow" style="left:1158px;top:1610px"><svg width="12" height="18"><path d="M2 2l7 7-7 7" fill="none" stroke="#222" stroke-width="3"/></svg></div>

<div class="abs card" style="left:60px">
  <div class="card-photo"><div role="img" aria-label="White sheets with a small print pattern" style="background:linear-gradient(170deg,#f4f4f6,#d6dbe4)"></div></div>
  <h5>Twin XL sheets</h5>
  <div class="stars"><svg width="110" height="20" viewBox="0 0 110 20"><g fill="var(--star)"><path id="st" d="M10 1l2.6 6 6.4.5-4.9 4.2 1.5 6.3L10 14.6 4.4 18l1.5-6.3L1 7.5l6.4-.5z"/><use href="#st" x="22"/><use href="#st" x="44"/><use href="#st" x="66"/></g><use href="#st" x="88" fill="var(--star-off)"/></svg></div>
</div>
<div class="abs card" style="left:340px">
  <div class="card-photo"><div role="img" aria-label="Light blue sheet set on a bed" style="background:linear-gradient(170deg,#8fa6c6,#5a739e)"></div></div>
  <h5>Olympic queen sheets</h5>
  <div class="stars"><svg width="110" height="20" viewBox="0 0 110 20"><g fill="var(--star)"><use href="#st"/><use href="#st" x="22"/><use href="#st" x="44"/></g><g fill="var(--star-off)"><use href="#st" x="66"/><use href="#st" x="88"/></g></svg></div>
</div>
<div class="abs card" style="left:620px">
  <div class="card-photo"><div role="img" aria-label="Bedroom with a green and yellow plaid bed set" style="background:linear-gradient(160deg,#e6d08a,#b9c86a 50%,#f0ead2)"></div></div>
  <h5>Twin XL sheets</h5>
  <div class="stars"><svg width="110" height="20" viewBox="0 0 110 20"><g fill="var(--star)"><use href="#st"/><use href="#st" x="22"/><use href="#st" x="44"/><use href="#st" x="66"/></g><use href="#st" x="88" fill="var(--star-off)"/></svg></div>
</div>
<div class="abs card" style="left:900px">
  <div class="card-photo"><div role="img" aria-label="Warm lit bedroom with a large bed" style="background:linear-gradient(160deg,#b04f2a,#e0a45c 50%,#f2e2a8)"></div></div>
  <h5>California King sheets</h5>
  <div class="stars"><svg width="110" height="20" viewBox="0 0 110 20"><g fill="var(--star)"><use href="#st"/><use href="#st" x="22"/><use href="#st" x="44"/><use href="#st" x="66"/></g><use href="#st" x="88" fill="var(--star-off)"/></svg></div>
</div>

<!-- footer band -->
<section class="abs band" aria-label="Footer information"></section>
<div class="abs tips">
  <div class="col-title">Bed Sheet Buying Tips</div>
  <div class="tip"><span class="tip-num">1</span><p>Higher thread count sheets are usually softer, but aren't always the best. If you like a cooler, lighter sheet then shop in the 200 to 500 range. If you're looking for the ultimate in bedding softness, opt for a sateen weave.</p></div>
  <div class="tip"><span class="tip-num">2</span><p>If you're buying <a><b>Olympic Queen sheets</b></a>, consider buying just an Olympic Queen fitted sheet to save money if you already have a Queen sheet set.</p></div>
  <div class="tip"><span class="tip-num">3</span><p>The above also goes for California King sheets too. You may only have to buy a <a><b>California King fitted sheet</b></a> if you already have a King bedding set.</p></div>
  <div class="tip"><span class="tip-num">4</span><p>The type of cotton matters. Only look for <a><b>Pima and Egyptian cotton</b></a> as these are the best long-staple cottons.</p></div>
</div>
<div class="abs chirp">
  <div class="col-title"><svg width="22" height="22"><rect width="22" height="22" rx="3" fill="#bbb"/></svg>Chirpline</div>
  <div class="tweet"><span class="q">&ldquo;</span><p>Lorem Ipsum is simply dummy text of the printing and typesetting industry. <a><b>Lorem Ipsum</b></a> has been the indus-<br><small>2 hour ago</small></p></div>
  <div class="tweet"><span class="q">&ldquo;</span><p>Lorem Ipsum is simply dummy text of the printing and typesetting industry. <a><b>Lorem Ipsum</b></a> has been the indus-<br><small>3 days ago</small></p></div>
  <div class="tweet"><span class="q">&ldquo;</span><p>Lorem Ipsum is simply dummy text of the printing and typesetting industry. <a><b>Lorem Ipsum</b></a> has been the indus-<br><small>3 days ago</small></p></div>
</div>
<div class="abs fans">
  <div class="col-title"><svg width="22" height="22"><rect width="22" height="22" rx="3" fill="#bbb"/></svg>Friendwall</div>
  <p>500 people like Lume Swathe</p>
  <div class="fan-grid">
    <div><span role="img" aria-label="Member avatar"></span>Arne</div>
    <div><span role="img" aria-label="Member avatar"></span>Arne</div>
    <div><span role="img" aria-label="Member avatar"></span>Arne</div>
    <div><span role="img" aria-label="Member avatar"></span>Arne</div>
    <div><span role="img" aria-label="Member avatar"></span>Arne</div>
    <div><span role="img" aria-label="Member avatar"></span>Arne</div>
    <div><span role="img" aria-label="Member avatar"></span>Arne</div>
    <div><span role="img" aria-label="Member avatar"></span>Arne</div>
    <div><span role="img" aria-label="Member avatar"></span>Arne</div>
  </div>
</div>
<div class="abs foot-links"><a>Home</a>|<a>Learning Center</a>|<a>Terms of Use</a>|<a>Privacy</a>|<a>Returns</a>|<a>Contact Us</a>|<a>Login</a></div>
<div class="abs copy">© 2012 Lume Swathe. All Rights Reserved</div>

</body>
</html>
```